"Beyond Marrow Cay" Fictional Book Cover

BEYOND MARROW CAY
By: Dale Pruitt

Here's the intro .

"It had been nearly forty years since Ted Larraby last went to the island from where he was raised. Three months earlier he never would have thought about ever coming back. But life is weird. Things happen quickly and plans change, especially when your very life is at stake. The reason he was going back wasn’t to see old friends...no, no, no. They’re all dead. Of all the kids he grew up with on the island who moved off, he’s the only one still alive. Why?"

Pretty much all just a Lumeno book, by the way.

Target Market(s)

fiction readers

Requirements
Must have
• Somewhat of a dark, mysterious cover is what I'd like to see. Use your imagination. I've never written a fiction book before so I'm very open to ideas

Needs to have my name, DALE PRUITT at the bottom. like my other books, all of which are non-fiction
Nice to have
• Mysterious is what I'm looking for. NOT A HORROR story though. More a guy who left the island years ago, but is being called back to escape the rat race of modern, consumerist culture.

Please remember this NEEDS to jump out as a thumbnail on Bookvale as people are browsing. Mainly the WORDS need to stick out. Lighter words on a say a blue background.

If you want to try to use the attached pic, or something like this, to reflect an island in the cover, that'd be good.

I've also uploaded a couple images I purchased from Pixelcrate, hopefully you can make something work with these.

```html
<!DOCTYPE html>
<html lang="en">
<head>
<meta charset="utf-8">
<title>Beyond Marrow Cay — Dale Pruitt</title>
<link rel="stylesheet" href="https://fonts.googleapis.com/css2?family=Roboto+Slab:wght@900&family=Bebas+Neue&display=swap">
<style>
  :root {
    --frame-grey: #58585a;
    --cover-black: #0e0e0e;
    --sky-blue: #3f78b4;
    --sky-light: #7fa9d6;
    --sky-deep: #123152;
    --shore-dark: #1a2127;
    --title-white: #ffffff;
  }
  html, body {
    margin: 0;
    padding: 0;
    width: 840px;
    height: 1200px;
    overflow: hidden;
    background: var(--frame-grey);
  }
  .cover {
    position: absolute;
    left: 60px;
    top: 60px;
    width: 720px;
    height: 1080px;
    background: var(--cover-black);
    overflow: hidden;
  }
  .cover-photo {
    position: absolute;
    left: 0;
    top: 0;
    width: 720px;
    height: 505px;
    background: linear-gradient(180deg,
      var(--sky-deep) 0%,
      var(--sky-blue) 25%,
      var(--sky-light) 50%,
      var(--sky-blue) 68%,
      var(--shore-dark) 85%,
      var(--cover-black) 100%);
  }
  .title {
    position: absolute;
    left: 0;
    top: 532px;
    width: 720px;
    margin: 0;
    text-align: center;
    font-family: "Roboto Slab", "Rockwell", serif;
    font-weight: 900;
    font-size: 112px;
    line-height: 113px;
    letter-spacing: 0;
    color: var(--title-white);
  }
  .author {
    position: absolute;
    left: 0;
    top: 966px;
    width: 720px;
    margin: 0;
    text-align: center;
    font-family: "Bebas Neue", "Arial Narrow", sans-serif;
    font-weight: 400;
    font-size: 66px;
    line-height: 66px;
    letter-spacing: 1px;
    color: var(--title-white);
  }
</style>
</head>
<body>
  <main class="cover">
    <div class="cover-photo" role="img" aria-label="Photo: a large full moon rising over the sea at night, framed by dark trees and tall grass"></div>
    <h1 class="title">BEYOND<br>MARROW<br>CAY</h1>
    <p class="author">DALE PRUITT</p>
  </main>
</body>
</html>
```